Brochure folder for audio visual proposals

We're looking for a design for our A4 booklet. Print guideline file provided. The booklet is used for Audio Visual proposal submissions in corporate settings. I will supply all body copy, logo and some image options although also open to suggestions for suitable images or design features. Also attached the front cover from our proposals that will be sent inside these folders in the pocket for reference.
Hoping to achieve a sleek, classic looking folder communicates quality and technology that we can hopefully use for years to come.

Our website if you'd like more info or vibe of what we do www.tarnivox.com.au
Need final art delivered in vector.

Front Cover: Audio Visual Proposal our logo and cool design or use image
Inside top left panel: Microphone image with "Let's Get Started!" text
Bottom left: Just simple text in corner on 3 lines as below
Experienced.
Knowledgeable.
Trustworthy.
Inside right hand side: Top right is the 7" screen (colour code the play etc buttons with theme to suit
Bottom right Text TBC
Back Cover: Simple design office locations small logo, website, Pavlora, Glintory and Worvanta symbols

Target Market(s)

corporate events

Industry/Entity Type

audio visual

Requirements
Must have
• our logo. Title of "Audio Visual Proposal" on the cover
Should not have
• any other company branding. The PDF example was just for refence.

```html
<!DOCTYPE html>
<html lang="en">
<head>
<meta charset="utf-8">
<title>Audio Visual Proposal – Folder Cover</title>
<link rel="stylesheet" href="https://fonts.googleapis.com/css2?family=Montserrat:wght@800;900&family=Quicksand:wght@300;400&display=swap">
<style>
  :root {
    --page-bg: #ffffff;
    --cover-base: #2b2926;
    --cover-band: #34322f;
    --bubble: #3a3835;
    --accent-blue: #22aee6;
    --title-grey: #a4a4a6;
    --ring-glow: #2fc3e8;
    --photo-warm: #e9c9a3;
    --photo-denim: #4f7391;
    --photo-light: #f2ede6;
  }
  * { margin: 0; padding: 0; box-sizing: border-box; }
  html, body {
    width: 1200px; height: 1200px; overflow: hidden;
    background: var(--page-bg);
  }
  .folder-cover {
    position: absolute; left: 212px; top: 50px;
    width: 776px; height: 1100px;
    background: var(--cover-base);
    overflow: hidden;
  }
  .cover-decor { position: absolute; inset: 0; width: 100%; height: 100%; }
  .brand {
    position: absolute; left: 285px; top: 220px;
    display: flex; align-items: center; gap: 10px;
  }
  .brand-name {
    font-family: "Montserrat", sans-serif; font-weight: 900;
    font-size: 31px; letter-spacing: 0.02em;
    color: var(--accent-blue);
  }
  .brand-mark {
    width: 22px; height: 22px; border-radius: 50%;
    background: var(--accent-blue);
  }
  .cover-title {
    position: absolute; left: 178px; top: 385px; width: 410px;
  }
  .title-line {
    display: block;
    font-family: "Quicksand", sans-serif; font-weight: 300;
    font-size: 52px; line-height: 1; color: var(--title-grey);
    letter-spacing: 0.01em; white-space: nowrap;
  }
  .title-heading {
    display: flex; justify-content: space-between;
    margin-top: 18px;
    font-family: "Montserrat", sans-serif; font-weight: 900;
    font-size: 50px; line-height: 1; color: var(--accent-blue);
  }
  .cover-photo {
    position: absolute; left: 225px; top: 592px;
    width: 320px; height: 320px; border-radius: 50%;
    background:
      radial-gradient(circle at 22% 35%, var(--photo-light) 0%, rgba(242,237,230,0) 38%),
      radial-gradient(circle at 30% 85%, var(--photo-warm) 0%, rgba(233,201,163,0) 45%),
      linear-gradient(120deg, #c9b7a0 0%, var(--photo-denim) 55%, #3c5a74 100%);
    border: 3px solid var(--ring-glow);
    box-shadow: 0 0 14px 3px rgba(47,195,232,0.55);
  }
</style>
</head>
<body>
  <main class="folder-cover">
    <svg class="cover-decor" viewBox="0 0 776 1100" aria-hidden="true">
      <polygon class="band-top" fill="var(--cover-band)"
        points="0,0 776,0 776,180 760,50 265,42 210,160 0,225"/>
      <polygon class="band-bottom" fill="var(--cover-band)"
        points="0,1100 776,1100 776,870 620,905 560,1005 230,955 170,985 0,945"/>
      <circle class="bubble" cx="285" cy="313" r="14" fill="var(--bubble)"/>
      <circle class="bubble" cx="248" cy="364" r="23" fill="var(--bubble)" opacity="0.8"/>
      <circle class="bubble" cx="225" cy="427" r="38" fill="var(--bubble)" opacity="0.6"/>
      <circle class="bubble" cx="224" cy="495" r="54" fill="var(--bubble)" opacity="0.5"/>
      <circle class="bubble" cx="265" cy="605" r="105" fill="var(--bubble)" opacity="0.35"/>
      <ellipse class="bubble" cx="700" cy="960" rx="260" ry="210" fill="var(--bubble)" opacity="0.25"/>
    </svg>

    <div class="brand">
      <span class="brand-name">TARNIVOX</span>
      <span class="brand-mark"></span>
    </div>

    <h1 class="cover-title">
      <span class="title-line">Audio Visual</span>
      <span class="title-heading"><span>P</span><span>R</span><span>O</span><span>P</span><span>O</span><span>S</span><span>A</span><span>L</span></span>
    </h1>

    <div class="cover-photo" role="img"
      aria-label="Photo of a person in a denim shirt typing on a laptop while holding a phone with a video play overlay"></div>
  </main>
</body>
</html>
```